We need a fresh, new church business card!!

We need a church business card with basic info to hand out as invites. We are looking for something clean that communicates our basic information clearly.

We are open to square or rectangle card sizes.

General Public

Religious

The attached logo is the only one that I have available. We'd like to see options with with text of the logo lighter and on a dark background as well as options with white/light backgrounds.

Also, we'd like to see option with rounded corners.

• Address - 2718 Maple Row, Rockford, IL 61142
• Website - brookvane.example
• Phone - 815-555-0163
• Service times -
• Sunday - 10am Sunday School
• - 11am Family Worship
• - 6pm Night of Prayer
• Wednesday - 7:30pm Adult Bible Study
• Classes for all ages

```html
<!DOCTYPE html>
<html lang="en">
<head>
<meta charset="utf-8">
<title>Brookvane Pentecostal Church – Business Card</title>
<link href="https://fonts.googleapis.com/css2?family=Lato:wght@300;400&family=Roboto+Condensed:wght@400&family=Roboto+Slab:wght@600&display=swap" rel="stylesheet">
<style>
  :root {
    --backdrop: #a6a3a3;
    --teal: #5f96a6;
    --paper: #fbfbfb;
    --ink: #6d6d6d;
    --ink-soft: #7a7a7a;
    --band-grey: #8e8e8e;
    --white: #ffffff;
  }
  * { margin: 0; padding: 0; box-sizing: border-box; }
  html, body { width: 1200px; height: 1200px; overflow: hidden; }
  body { background: var(--backdrop); position: relative; font-family: "Lato", sans-serif; }

  .card { position: absolute; border-radius: 22px; overflow: hidden; }
  .card--front { left: 238px; top: 118px; width: 712px; height: 419px; background: var(--teal); }
  .card--back { left: 231px; top: 645px; width: 711px; height: 415px; background: var(--paper); }

  .wordmark { position: absolute; display: flex; align-items: center; }
  .wordmark__dot { border-radius: 50%; flex: none; }
  .wordmark__text { font-family: "Lato", sans-serif; font-weight: 400; line-height: 1; }
  .wordmark__name { display: block; letter-spacing: 1px; }
  .wordmark__sub { display: block; }

  .card--front .wordmark { left: 128px; top: 165px; }
  .card--front .wordmark__dot { width: 78px; height: 78px; background: var(--white); margin-right: 26px; }
  .card--front .wordmark__text { color: var(--white); }
  .card--front .wordmark__name { font-size: 58px; }
  .card--front .wordmark__sub { font-size: 16px; letter-spacing: 6.2px; margin-top: 10px; padding-left: 4px; }

  .card--back .wordmark { left: 167px; top: 55px; }
  .card--back .wordmark__dot { width: 64px; height: 64px; background: var(--teal); margin-right: 22px; }
  .card--back .wordmark__text { color: var(--ink); }
  .card--back .wordmark__name { font-size: 48px; }
  .card--back .wordmark__sub { font-size: 14px; letter-spacing: 5.2px; margin-top: 8px; padding-left: 4px; }

  .contact { position: absolute; left: 0; width: 100%; top: 168px; text-align: center;
    font-weight: 300; font-size: 18px; color: var(--ink-soft); line-height: 27px; letter-spacing: 0.3px; }
  .contact__sep { margin: 0 12px; }

  .services-title { position: absolute; left: 251px; top: 262px; width: 211px; height: 32px;
    border: 2px solid var(--teal); font-family: "Roboto Slab", serif; font-weight: 600;
    font-size: 19px; color: var(--ink); text-align: center; line-height: 28px; letter-spacing: 0.5px; }

  .services { position: absolute; left: 39px; top: 305px; font-family: "Roboto Condensed", sans-serif;
    font-size: 16.5px; color: var(--ink); line-height: 26px; }
  .services__day { color: var(--teal); }
  .services__sep { margin: 0 9px; }

  .card-band { position: absolute; left: 0; bottom: 0; }
  .card-band__label { position: absolute; right: 62px; bottom: 16px; font-family: "Roboto Slab", serif;
    font-weight: 600; font-size: 17px; color: var(--white); letter-spacing: 0.6px; }
</style>
</head>
<body>

  <section class="card card--front" aria-label="Card front">
    <div class="wordmark">
      <span class="wordmark__dot"></span>
      <span class="wordmark__text">
        <span class="wordmark__name">BROOKVANE</span>
        <span class="wordmark__sub">PENTECOSTAL CHURCH</span>
      </span>
    </div>
  </section>

  <section class="card card--back" aria-label="Card back">
    <div class="wordmark">
      <span class="wordmark__dot"></span>
      <span class="wordmark__text">
        <span class="wordmark__name">BROOKVANE</span>
        <span class="wordmark__sub">PENTECOSTAL CHURCH</span>
      </span>
    </div>

    <p class="contact">
      815-555-0163<span class="contact__sep">|</span>www.brookvane.example<br>
      2718 Maple Row, Rockford, IL 61142
    </p>

    <h2 class="services-title">SERVICE TIMES</h2>

    <div class="services">
      <p><span class="services__day">SUNDAY</span> Sunday School .. 10:00am<span class="services__sep">|</span>Family Worship .. 11:00am<span class="services__sep">|</span>Night of Prayer .. 6:00pm</p>
      <p><span class="services__day">WEDNESDAY</span> Adult Bible Study ... 7:30pm</p>
    </div>

    <svg class="card-band" width="711" height="60" viewBox="0 0 711 60" aria-hidden="true">
      <rect x="0" y="30" width="360" height="30" fill="var(--band-grey)"/>
      <polygon points="327,60 364,5 711,5 711,60" fill="var(--teal)"/>
    </svg>
    <p class="card-band__label">CLASSES FOR ALL AGES</p>
  </section>

</body>
</html>
```